Graphic background for 10 Pull Up Banners

To produce a graphic background for a 100 cm wide by 200 cm high Pull-Up Display banner containing a Buddhist text in three languages: Tibetan, Mandarin and English. Please refer to uploaded file "Elements of Pull Up Banner". The design should be simple (not drawing attention away from the text). This design should then be varied for or extended to the next banner and so on until the 10th banner. When the banners are lined up, they should form a single design that is 1000 cm wide by 200 cm high.
An alternative way to look at the project is to produce a graphic background of 1000 cm width by 200 cm height that is then splitted into ten separate 100 cm wide by 200 cm high graphic to be used as background for 10 Buddhist texts (text 1, 2, 3, 4, 5, 6, 7, 8, 9a, 9b) on 10 Pull-Up Display Banners, the text in each banner being in the three languages mentioned earlier.
In either perspective, the design should be simple and not draw attention away from the texts. See uploaded PDF file "Examples.pdf"
For attendees at a Buddhist Event.

```html
<!DOCTYPE html>
<html lang="en">
<head>
<meta charset="utf-8">
<title>Pull-Up Banner Series</title>
<link rel="stylesheet" href="https://fonts.googleapis.com/css2?family=Oranienbaum&family=Noto+Serif+SC:wght@400&family=Noto+Serif+Tibetan&display=swap">
<style>
  :root {
    --green-deep: #86c540;
    --green-mid: #b3d63a;
    --green-light: #cfe04a;
    --yellow-glow: #f2ea3a;
    --title-red: #b8142e;
    --frame-white: rgba(255,255,255,0.95);
    --plaque-fill: rgba(255,250,190,0.45);
    --plaque-line: rgba(255,255,255,0.8);
    --emblem-tone: #c9a13a;
  }
  * { box-sizing: border-box; margin: 0; padding: 0; }
  html, body { width: 1200px; height: 494px; overflow: hidden; background: #fff; }
  .banner-strip {
    position: relative; width: 1200px; height: 494px; overflow: hidden;
    background:
      radial-gradient(ellipse 900px 120px at 50% 500px, rgba(242,234,58,0.75), transparent 70%),
      linear-gradient(90deg, var(--green-deep) 0%, var(--green-mid) 45%, var(--green-light) 100%);
  }
  .waves { position: absolute; left: 0; top: 0; width: 1200px; height: 494px; }
  .bokeh { position: absolute; border-radius: 50%; background: rgba(255,255,255,0.18); }
  .banner { position: absolute; top: 0; width: 242px; height: 494px; }
  .banner + .banner { border-left: 1px solid rgba(255,255,255,0.25); }
  .frame { position: absolute; left: 0; top: 0; }
  .emblem {
    position: absolute; left: 20px; top: 42px; width: 48px; height: 56px;
    border-radius: 22px 22px 6px 6px;
    background: linear-gradient(180deg, rgba(201,161,58,0.55), rgba(184,20,46,0.35));
  }
  .title {
    position: absolute; font-family: "Oranienbaum", "Times New Roman", serif;
    color: var(--title-red); line-height: 0.9; white-space: nowrap;
  }
  .title .big { font-size: 27px; display: block; }
  .title .small { font-size: 14px; }
  .plaque {
    position: absolute; left: 50px; top: 408px; width: 142px; height: 55px;
    background: var(--plaque-fill); border: 1px solid var(--plaque-line);
    outline: 1px solid rgba(255,255,255,0.5); outline-offset: -4px;
    text-align: center; color: var(--title-red); padding-top: 9px;
  }
  .plaque .tibetan { font-family: "Noto Serif Tibetan", serif; font-size: 7px; line-height: 10px; word-spacing: 12px; }
  .plaque .chinese { font-family: "Noto Serif SC", serif; font-size: 7.5px; line-height: 11px; }
  .plaque .english { font-family: "Times New Roman", serif; font-size: 7px; line-height: 10px; }
</style>
</head>
<body>
<div class="banner-strip">
  <svg class="waves" viewBox="0 0 1200 494" aria-hidden="true">
    <g fill="none" stroke="rgba(255,255,255,0.22)" stroke-width="1">
      <path d="M0 400 C200 360 400 440 600 400 S1000 360 1200 390"/>
      <path d="M0 412 C220 372 420 452 620 410 S1010 372 1200 402"/>
      <path d="M0 430 C180 400 380 470 600 430 S980 400 1200 420"/>
      <path d="M0 445 C250 415 450 480 650 445 S1000 420 1200 440"/>
      <path d="M0 460 C230 440 430 490 640 462 S1020 440 1200 458"/>
    </g>
  </svg>
  <div class="bokeh" style="left:108px;top:375px;width:80px;height:80px"></div>
  <div class="bokeh" style="left:150px;top:395px;width:50px;height:50px"></div>
  <div class="bokeh" style="left:735px;top:340px;width:70px;height:70px"></div>
  <div class="bokeh" style="left:860px;top:355px;width:60px;height:60px"></div>
  <div class="bokeh" style="left:1130px;top:310px;width:70px;height:70px"></div>
  <div class="bokeh" style="left:1070px;top:340px;width:40px;height:40px"></div>

  <!-- Banner 1 -->
  <section class="banner" style="left:0">
    <svg class="frame" width="242" height="494" viewBox="0 0 242 494" aria-hidden="true">
      <path d="M22 6 H221 A16 16 0 0 0 237 22 V468 A16 16 0 0 0 221 484 H22 A16 16 0 0 0 6 468 V22 A16 16 0 0 0 22 6 Z" fill="none" stroke="var(--frame-white)" stroke-width="1"/>
    </svg>
    <div class="emblem" role="img" aria-label="Golden seated Buddha emblem"></div>
    <h2 class="title" style="left:77px;top:58px"><span class="big">Ten Mistaking</span></h2>
    <div class="plaque"><p class="tibetan">སེམས་ཅན་ སངས་རྒྱས་</p><p class="chinese">愿诸有情共证佛果位</p><p class="english">May all attain Buddhahood together.</p></div>
  </section>

  <!-- Banner 2 -->
  <section class="banner" style="left:242px">
    <svg class="frame" width="242" height="494" viewBox="0 0 242 494" aria-hidden="true">
      <path d="M22 6 H221 A16 16 0 0 0 237 22 V468 A16 16 0 0 0 221 484 H22 A16 16 0 0 0 6 468 V22 A16 16 0 0 0 22 6 Z" fill="none" stroke="var(--frame-white)" stroke-width="1"/>
    </svg>
    <div class="emblem" role="img" aria-label="Golden seated Buddha emblem"></div>
    <h2 class="title" style="left:100px;top:40px">
      <span class="big">Desire <span class="small" style="font-size:18px">&amp;</span></span>
      <span class="big">Attachment</span>
    </h2>
    <div class="plaque"><p class="tibetan">སེམས་ཅན་ སངས་རྒྱས་</p><p class="chinese">愿诸有情共证佛果位</p><p class="english">May all attain Buddhahood together.</p></div>
  </section>

  <!-- Banner 3 -->
  <section class="banner" style="left:484px">
    <svg class="frame" width="242" height="494" viewBox="0 0 242 494" aria-hidden="true">
      <path d="M22 6 H221 A16 16 0 0 0 237 22 V468 A16 16 0 0 0 221 484 H22 A16 16 0 0 0 6 468 V22 A16 16 0 0 0 22 6 Z" fill="none" stroke="var(--frame-white)" stroke-width="1"/>
    </svg>
    <div class="emblem" role="img" aria-label="Golden seated Buddha emblem"></div>
    <h2 class="title" style="left:69px;top:48px;text-align:center">
      <span class="small" style="font-size:12.5px;display:block">Signs Of Having Practised</span>
      <span class="big" style="font-size:30px">The Dharma</span>
    </h2>
    <div class="plaque"><p class="tibetan">སེམས་ཅན་ སངས་རྒྱས་</p><p class="chinese">愿诸有情共证佛果位</p><p class="english">May all attain Buddhahood together.</p></div>
  </section>

  <!-- Banner 4 -->
  <section class="banner" style="left:726px">
    <svg class="frame" width="242" height="494" viewBox="0 0 242 494" aria-hidden="true">
      <path d="M22 6 H221 A16 16 0 0 0 237 22 V468 A16 16 0 0 0 221 484 H22 A16 16 0 0 0 6 468 V22 A16 16 0 0 0 22 6 Z" fill="none" stroke="var(--frame-white)" stroke-width="1"/>
    </svg>
    <div class="emblem" role="img" aria-label="Golden seated Buddha emblem"></div>
    <h2 class="title" style="left:76px;top:36px">
      <span class="big">Kindness</span>
      <span class="big"><span class="small" style="font-size:16px;padding-left:26px">Of The</span> Guru</span>
    </h2>
    <div class="plaque"><p class="tibetan">སེམས་ཅན་ སངས་རྒྱས་</p><p class="chinese">愿诸有情共证佛果位</p><p class="english">May all attain Buddhahood together.</p></div>
  </section>

  <!-- Banner 5 -->
  <section class="banner" style="left:968px">
    <svg class="frame" width="242" height="494" viewBox="0 0 242 494" aria-hidden="true">
      <path d="M22 6 H221 A16 16 0 0 0 237 22 V468 A16 16 0 0 0 221 484 H22 A16 16 0 0 0 6 468 V22 A16 16 0 0 0 22 6 Z" fill="none" stroke="var(--frame-white)" stroke-width="1"/>
    </svg>
    <div class="emblem" role="img" aria-label="Golden seated Buddha emblem"></div>
    <h2 class="title" style="left:78px;top:44px;text-align:center">
      <span class="big" style="font-size:23px">You And</span>
      <span class="big">The Dharma</span>
    </h2>
    <div class="plaque"><p class="tibetan">སེམས་ཅན་ སངས་རྒྱས་</p><p class="chinese">愿诸有情共证佛果位</p><p class="english">May all attain Buddhahood together.</p></div>
  </section>
</div>
</body>
</html>
```